Business Card Design Project

Construction

Industry/Entity Type

Business

Contact Information for Business Card

I've had the same logo for about 5 years. The logo itself is fine, however I'm looking to get a new design on the card. The green for the log is fine but the grey for the rest of the card is kind of dark and blah. Would like a new look. I'll send the file with the logo.

```html
<!DOCTYPE html>
<html lang="en">
<head>
<meta charset="utf-8">
<title>Northfield Commercial Builders – Business Card</title>
<link rel="stylesheet" href="https://fonts.googleapis.com/css2?family=Roboto:wght@400;500;700;900&family=Roboto+Condensed:wght@700&display=swap">
<style>
  :root {
    --backdrop: #2a2a2a;
    --card-white: #f4f4f4;
    --brand-green: #18c43c;
    --deep-green: #0a8f1f;
    --green-light: #1cb534;
    --text-grey: #4d4d4d;
    --text-dark: #111111;
    --white: #ffffff;
    --badge-grey: #8f8f8f;
  }
  * { margin: 0; padding: 0; box-sizing: border-box; }
  html, body { width: 1200px; height: 960px; overflow: hidden; }
  body {
    background: var(--backdrop);
    font-family: "Roboto", Arial, sans-serif;
    position: relative;
  }
  .card {
    position: absolute;
    width: 600px;
    height: 343px;
    box-shadow: 0 4px 10px rgba(0,0,0,0.5);
  }
  .card-front { left: 314px; top: 113px; background: var(--card-white); }
  .card-back {
    left: 311px; top: 472px;
    background: radial-gradient(ellipse at 35% 35%, var(--green-light) 0%, var(--deep-green) 75%);
    color: var(--white);
  }

  /* brand name lockup */
  .brand { position: absolute; display: flex; align-items: center; gap: 8px; }
  .brand-mark { flex: none; }
  .brand-name {
    font-weight: 900;
    line-height: 1.1;
    letter-spacing: 0.2px;
    text-transform: uppercase;
    white-space: nowrap;
  }
  .card-front .brand { left: 50px; top: 152px; }
  .card-front .brand-mark { width: 18px; height: 18px; background: var(--brand-green); }
  .card-front .brand-name { color: var(--text-dark); font-size: 14px; }
  .card-back .brand { left: 30px; top: 150px; }
  .card-back .brand-mark { width: 22px; height: 22px; background: var(--text-dark); }
  .card-back .brand-name { color: var(--text-dark); font-size: 20px; }

  /* front */
  .service-badge {
    position: absolute; right: 14px; top: 22px;
    width: 108px; height: 38px;
    border-radius: 4px;
    background: var(--badge-grey);
  }
  .divider { position: absolute; left: 272px; top: 86px; width: 2px; height: 180px;
    background: linear-gradient(to bottom, #bdbdbd, rgba(189,189,189,0)); }
  .divider-accent { position: absolute; left: 272px; top: 86px; width: 5px; height: 34px; background: var(--brand-green); }
  .contact-block { position: absolute; left: 298px; top: 84px; }
  .person-name { font-family: "Roboto Condensed", "Roboto", sans-serif; font-weight: 700; font-size: 21px; color: var(--brand-green); line-height: 1.1; }
  .person-title { font-weight: 500; font-size: 16px; color: var(--text-grey); margin-top: 2px; letter-spacing: 0.3px; }
  .contact-list { list-style: none; margin-top: 12px; font-size: 14.5px; color: var(--text-grey); line-height: 19.5px; }
  .service-area { margin-top: 6px; font-weight: 700; font-size: 14.5px; color: var(--brand-green); line-height: 18px; text-transform: uppercase; letter-spacing: 0.2px; }

  /* back */
  .back-contact { position: absolute; left: 29px; top: 219px; font-size: 14.5px; line-height: 19.5px; }
  .back-contact p + p { margin-top: 5px; }
  .cert-badges { position: absolute; right: 24px; top: 32px; display: flex; gap: 8px; }
  .cert-badge { width: 72px; height: 72px; border-radius: 50%; background: var(--text-dark); border: 4px solid var(--white); box-shadow: 0 0 0 1.5px var(--text-dark); }
  .info-block { position: absolute; right: 25px; text-align: right; }
  .licenses { top: 136px; }
  .naics { top: 260px; }
  .info-heading { font-weight: 700; font-size: 17px; margin-bottom: 7px; letter-spacing: 0.2px; }
  .license-list { list-style: none; font-size: 14.5px; line-height: 19.3px; }
  .license-list li::after { content: ""; display: inline-block; width: 6px; height: 6px; background: var(--white); margin-left: 11px; vertical-align: 2px; }
  .naics-codes { font-size: 14.5px; line-height: 19.5px; }
</style>
</head>
<body>

<section class="card card-front" aria-label="Business card front">
  <div class="service-badge" role="img" aria-label="Years of service badge"></div>

  <div class="brand">
    <span class="brand-mark"></span>
    <span class="brand-name">Northfield<br>Commercial Builders</span>
  </div>

  <div class="divider"></div>
  <div class="divider-accent"></div>

  <div class="contact-block">
    <h1 class="person-name">MARCUS HALE, DMP</h1>
    <p class="person-title">PRESIDENT</p>
    <ul class="contact-list">
      <li>P. (310) 555-0142</li>
      <li>P. (310) 555-0187</li>
      <li>Marcus@northfieldcommercial.com</li>
      <li>License# 1048271</li>
    </ul>
    <p class="service-area">Serving all of<br>Southern California</p>
  </div>
</section>

<section class="card card-back" aria-label="Business card back">
  <div class="brand">
    <span class="brand-mark"></span>
    <span class="brand-name">Northfield<br>Commercial Builders</span>
  </div>

  <div class="back-contact">
    <p>(310) 555-0163<br>(310) 555-0187</p>
    <p>NORTHFIELDCOMMERCIAL.com</p>
    <p>LICENSED, BONDED, INSURED<br>LICENSE# 1048271</p>
  </div>

  <div class="cert-badges">
    <span class="cert-badge" role="img" aria-label="Certification badge"></span>
    <span class="cert-badge" role="img" aria-label="Certification badge"></span>
  </div>

  <div class="info-block licenses">
    <h2 class="info-heading">LICENSES</h2>
    <ul class="license-list">
      <li>A - General Engineering</li>
      <li>B &nbsp;- General Building</li>
      <li>C21 - Demo/Bldg.moving</li>
      <li>C36 - Plumbing</li>
    </ul>
  </div>

  <div class="info-block naics">
    <h2 class="info-heading">NAICS CODES</h2>
    <p class="naics-codes">236220, 238110, 236118<br>23810, 238350, 238390, 327320</p>
  </div>
</section>

</body>
</html>
```